Market Intelligence Modules

Take the existing power point and add graphics to each slide and use photos and graphics to create a power point presentation that has the look and feel of a high tech company / research - with a theme of commercial real estate. To learn more about what the company does you can go to www.quarvelonix.com.

Target Market(s)

Target market are financial institutions and commercial real estate developers - going for high tech research look and feel and showing commercial real estate. ONLY commercial real estate.

Industry/Entity Type

Real Estate

Requirements
Must have
• Must have Quarvelonix logo and must communicate that Quarvelonix can process large amounts of data and analytics. Each slide should have some type of image that represents data or commercial real estate.
Should not have
• No blank white slides.

```html
<!DOCTYPE html>
<html lang="en">
<head>
<meta charset="utf-8">
<title>The Zettabyte Era</title>
<link rel="stylesheet" href="https://fonts.googleapis.com/css2?family=Roboto+Condensed:wght@700&family=Arimo:wght@400;700&display=swap">
<style>
  :root{
    --green:#2fa82c;
    --green-bright:#22b01f;
    --ink:#1c1c1c;
    --blue:#2b78c2;
    --faint:#d9dee3;
    --panel:#f1f2f4;
    --rule:#cfd3d8;
    --white:#ffffff;
  }
  *{margin:0;padding:0;box-sizing:border-box}
  html,body{width:1200px;height:900px;overflow:hidden;background:var(--white)}
  .slide{position:relative;width:1200px;height:900px;font-family:"Arimo",Arial,sans-serif;color:var(--ink)}
  .title-tab{position:absolute;left:0;top:18px;width:366px;height:57px}
  .title-tab span{position:absolute;left:36px;top:8px;font-family:"Roboto Condensed",Arial,sans-serif;font-weight:700;font-size:34px;color:var(--white)}
  .heading{position:absolute;left:63px;top:148px;font-family:"Roboto Condensed",Arial,sans-serif;font-weight:700;font-size:31px;color:var(--green)}
  .facts{position:absolute;left:93px;top:211px;list-style:none}
  .facts li{position:relative;padding-left:27px;font-size:21.5px;line-height:27px;margin-bottom:27px;white-space:nowrap}
  .facts li::before{content:"";position:absolute;left:0;top:8px;width:8px;height:8px;border-right:3px solid var(--green);border-top:3px solid var(--green);transform:rotate(45deg)}
  .scale-chart{position:absolute;left:78px;top:393px;width:345px;height:399px}
  .unit-table{position:absolute;left:447px;top:397px;width:696px;height:393px;background:var(--panel)}
  .unit-row{display:flex;align-items:center;height:54.5px;border-bottom:2px solid var(--rule);background:linear-gradient(#fafafa,#eef0f2)}
  .unit-name{width:221px;padding-left:21px;font-size:28px;color:#3a3a3a}
  .unit-value{font-size:28px;font-weight:700;letter-spacing:.3px;color:var(--faint)}
  .unit-value b{color:var(--blue)}
  .source-note{position:absolute;right:22px;bottom:6px;font-size:7px;letter-spacing:1px;color:#9aa}
  .footer-rule{position:absolute;left:0;top:822px;width:1200px;height:2px;background:#e3e3e3}
  .copyright{position:absolute;left:18px;top:855px;font-size:19px;color:var(--ink)}
  .brand{position:absolute;right:22px;top:840px;font-family:"Arimo",Arial,sans-serif;font-weight:700;font-size:36px;color:var(--green-bright)}
</style>
</head>
<body>
<div class="slide">
  <div class="title-tab">
    <svg width="366" height="57" viewBox="0 0 366 57"><polygon points="0,0 338,0 366,28.5 338,57 0,57" fill="var(--green-bright)"/></svg>
    <span>The Zettabyte Era</span>
  </div>

  <h2 class="heading">What is a zettabyte?</h2>
  <ul class="facts">
    <li>One zettabyte of data allows you to stack books from Earth to Pluto 20 times (72 billion miles)</li>
    <li>If one gigabyte of data were a cup of coffee a zettabyte would equal the Great Wall of China</li>
    <li>In 2015 all internet traffic will exceed one zettabyte of data - 540,000 time increase from 2003</li>
  </ul>

  <svg class="scale-chart" viewBox="0 0 345 399" role="img" aria-label="Data unit scale from megabytes up to one zettabyte">
    <rect width="345" height="399" fill="#f4f5f6"/>
    <g font-family="Arimo, Arial, sans-serif" font-weight="700" font-size="12" text-anchor="middle" fill="#222">
      <rect x="12" y="8" width="321" height="40" fill="#5a5a5a"/>
      <rect x="95" y="17" width="155" height="22" fill="#fff"/><text x="172" y="32">1000 MEGABYTES = 1GB</text>
      <path d="M12 50 L12 60 L333 60 L333 50 M172 60 L172 72" stroke="#555" stroke-width="2" fill="none"/>
      <rect x="12" y="78" width="321" height="40" fill="#7fd0ec"/>
      <rect x="95" y="87" width="155" height="22" fill="#fff"/><text x="172" y="102">1000 GIGABYTES = 1TB</text>
      <path d="M12 120 L12 130 L333 130 L333 120 M172 130 L172 142" stroke="#4bb8e0" stroke-width="2" fill="none"/>
      <rect x="12" y="148" width="321" height="40" fill="#f6b98a"/>
      <rect x="95" y="157" width="155" height="22" fill="#fff"/><text x="172" y="172">1000 TERABYTES = 1PB</text>
      <path d="M12 190 L12 200 L333 200 L333 190 M172 200 L172 212" stroke="#f09a5a" stroke-width="2" fill="none"/>
      <rect x="12" y="218" width="321" height="40" fill="#ee7aa4"/>
      <rect x="95" y="227" width="155" height="22" fill="#fff"/><text x="172" y="242">1000 PETABYTES = 1EB</text>
      <path d="M12 260 L12 270 L333 270 L333 260 M172 270 L172 282" stroke="#e4508a" stroke-width="2" fill="none"/>
      <rect x="12" y="288" width="321" height="40" fill="#d6ea9a"/>
      <rect x="78" y="297" width="190" height="22" fill="#fff"/><text x="172" y="312">1000 EXABYTES = 1 ZETTABYTE</text>
      <path d="M12 330 L12 340 L333 340 L333 330 M172 340 L172 354" stroke="#b8d86a" stroke-width="2" fill="none"/>
      <rect x="155" y="356" width="34" height="24" fill="#aaa"/><text x="172" y="373" font-size="11">1ZB</text>
    </g>
  </svg>

  <div class="unit-table">
    <div class="unit-row"><span class="unit-name">1 kilobyte</span><span class="unit-value"><b>1,000</b>,000,000,000,000,000,000</span></div>
    <div class="unit-row"><span class="unit-name">1 megabyte</span><span class="unit-value"><b>1,000,000</b>,000,000,000,000,000</span></div>
    <div class="unit-row"><span class="unit-name">1 gigabyte</span><span class="unit-value"><b>1,000,000,000</b>,000,000,000,000</span></div>
    <div class="unit-row"><span class="unit-name">1 terabyte</span><span class="unit-value"><b>1,000,000,000,000</b>,000,000,000</span></div>
    <div class="unit-row"><span class="unit-name">1 petabyte</span><span class="unit-value"><b>1,000,000,000,000,000</b>,000,000</span></div>
    <div class="unit-row"><span class="unit-name">1 exabyte</span><span class="unit-value"><b>1,000,000,000,000,000,000</b>,000</span></div>
    <div class="unit-row"><span class="unit-name">1 zettabyte</span><span class="unit-value"><b>1,000,000,000,000,000,000,000</b></span></div>
    <span class="source-note">SOURCE: VELTRANO</span>
  </div>

  <div class="footer-rule"></div>
  <p class="copyright">Copyright text here</p>
  <div class="brand">Quarvelonix</div>
</div>
</body>
</html>
```